Post storm repair flyer

looking for an eye catching 6x9 postcard to send out to single family home owners advertising a "Post Storm Repair Special" explaining that after the recent hurricanes its very important to have your roof checked and any repairs fixed right away before they become a bigger more costly problem and that even though your home wasn't directly hit by the storm the high wind gust could've cause unseen damage.
offer $200 off any repair *some rules may apply
Crest Roofing
877.612.LOFT
www.LoftRoofingco.example

```html
<!DOCTYPE html>
<html lang="en">
<head>
<meta charset="UTF-8">
<title>Crest Roofing – Post Storm Repair Special</title>
<link href="https://fonts.googleapis.com/css2?family=Montserrat:wght@400;500;600&family=Passion+One:wght@700&display=swap" rel="stylesheet">
<style>
  :root {
    --paper: #ffffff;
    --ink: #111111;
    --brand-grey: #2e2e2e;
    --muted: #444444;
  }
  html, body {
    margin: 0;
    padding: 0;
    overflow: hidden;
    background: var(--paper);
  }
  .postcard-back {
    position: relative;
    width: 800px;
    height: 1200px;
    background: var(--paper);
    color: var(--ink);
    overflow: hidden;
  }
  .centered {
    position: absolute;
    left: 0;
    width: 800px;
    margin: 0;
    text-align: center;
  }
  .special-title {
    top: 34px;
    font-family: "Passion One", sans-serif;
    font-weight: 700;
    font-size: 50px;
    line-height: 58px;
    letter-spacing: 1px;
  }
  .storm-message {
    position: absolute;
    top: 100px;
    left: 70px;
    width: 660px;
    margin: 0;
    text-align: center;
    font-family: "Montserrat", sans-serif;
    font-weight: 400;
    font-size: 16px;
    line-height: 22px;
    color: var(--muted);
  }
  .brand-mark {
    position: absolute;
    left: 350px;
    top: 230px;
    width: 100px;
    height: 100px;
    background: var(--ink);
  }
  .brand-name {
    top: 470px;
    font-family: "Montserrat", sans-serif;
    font-weight: 500;
    font-size: 40px;
    line-height: 50px;
    letter-spacing: 1px;
    color: var(--brand-grey);
  }
  .call-to-action {
    position: absolute;
    top: 596px;
    left: 60px;
    width: 680px;
    margin: 0;
    text-align: center;
    font-family: "Montserrat", sans-serif;
    font-weight: 400;
    font-size: 32px;
    line-height: 46px;
  }
  .contact-phone {
    top: 796px;
    font-family: "Passion One", sans-serif;
    font-weight: 700;
    font-size: 62px;
    line-height: 72px;
    letter-spacing: 1px;
  }
  .contact-web {
    top: 900px;
    font-family: "Passion One", sans-serif;
    font-weight: 700;
    font-size: 48px;
    line-height: 58px;
  }
  .offer {
    top: 1000px;
    font-family: "Passion One", sans-serif;
    font-weight: 700;
    font-size: 56px;
    line-height: 64px;
  }
  .fine-print {
    top: 1076px;
    font-family: "Montserrat", sans-serif;
    font-weight: 400;
    font-size: 16px;
    line-height: 22px;
    color: var(--muted);
  }
</style>
</head>
<body>
  <main class="postcard-back">
    <h2 class="centered special-title">POST STORM REPAIR SPECIAL</h2>
    <p class="storm-message">After the recent hurricanes, it is vital to have your roof checked. Even if your home wasn't directly hit, high wind gusts could have caused unseen damage. Fix it now, before it becomes a bigger, more costly problem.</p>
    <div class="brand-mark" aria-hidden="true"></div>
    <h1 class="centered brand-name">CREST ROOFING</h1>
    <p class="call-to-action">Protect your home today<br>—schedule your inspection with<br>Crest Roofing now!</p>
    <p class="centered contact-phone">877.612.LOFT</p>
    <p class="centered contact-web">WWW.LOFTROOFINGCO.EXAMPLE</p>
    <p class="centered offer">$200 OFF ANY REPAIR*</p>
    <p class="centered fine-print">*Some rules may apply.</p>
  </main>
</body>
</html>
```